Convert Adobe illustrator file to tri fold brochure

I have a line card that I need converted to a tri-fold brochure. I will fill in content details myself. I have uploaded the line card, please let me know if you have any questions.

```html
<!DOCTYPE html>
<html lang="en">
<head>
<meta charset="utf-8">
<title>Services Brochure – Inside Spread</title>
<link href="https://fonts.googleapis.com/css2?family=Montserrat:wght@700;800&family=Cabin:ital,wght@0,400;0,600;1,400&family=Barlow+Semi+Condensed:wght@600;700&display=swap" rel="stylesheet">
<style>
  :root {
    --orange: #ef6a12;
    --orange-deep: #e2531a;
    --orange-light: #f7941d;
    --peach: #fde3d4;
    --grey-band: #d9d9d9;
    --slate: #4a4a4a;
    --ink: #1e1e1e;
    --white: #ffffff;
  }
  * { box-sizing: border-box; margin: 0; padding: 0; }
  html, body { width: 1200px; height: 927px; overflow: hidden; background: var(--white); }
  .spread { position: relative; width: 1200px; height: 927px; overflow: hidden; background: var(--white);
    font-family: "Cabin", "Gill Sans", sans-serif; color: var(--ink); }

  .band { position: absolute; }
  .band--peach { background: var(--peach); }
  .band--grey { background: var(--grey-band); }

  .section-head { position: absolute; height: 60px; display: flex; align-items: center; }
  .section-head__bar { position: absolute; inset: 0;
    background: linear-gradient(90deg, var(--orange-deep), var(--orange) 55%, var(--orange-light));
    clip-path: polygon(0 0, 100% 0, calc(100% - 34px) 100%, 0 100%); }
  .section-head__stripe { position: absolute; top: 0; right: -14px; width: 34px; height: 60px; background: var(--slate);
    clip-path: polygon(20px 0, 34px 0, 14px 60px, 0 60px); }
  .section-head__title { position: relative; font-family: "Montserrat", sans-serif; font-weight: 800;
    color: var(--white); font-size: 21px; line-height: 26px; text-align: center; letter-spacing: 0.3px; }
  .section-head__icon { position: absolute; top: 5px; width: 50px; height: 50px; }

  .copy { position: absolute; font-size: 15.5px; line-height: 22px; }
  .copy p { margin-bottom: 22px; }
  .label { font-family: "Barlow Semi Condensed", sans-serif; font-weight: 700; font-size: 16.5px; }
  .callout { font-style: italic; text-align: center; font-size: 21px; line-height: 29px; }
  .callout--orange { color: var(--orange); }
  .callout--dark { color: var(--ink); }
  .emphasis { color: var(--orange); font-weight: 700; font-style: italic; }

  .fruit-photo { position: absolute; left: 36px; top: 850px; width: 320px; height: 66px;
    background: linear-gradient(90deg, #8e1414 0 17%, transparent 17% 20%, #f29415 20% 36%, transparent 36% 40%, #8e1414 40% 57%, transparent 57% 60%, #8b1212 60% 77%, transparent 77% 80%, #8e1414 80% 97%, transparent 97%);
    border-radius: 30px; opacity: .9; }
</style>
</head>
<body>
<main class="spread">
  <!-- background bands -->
  <div class="band band--peach" style="left:238px;top:0;width:172px;height:927px"></div>
  <div class="band band--peach" style="left:515px;top:0;width:175px;height:480px"></div>
  <div class="band band--peach" style="left:515px;top:660px;width:260px;height:267px"></div>
  <div class="band band--peach" style="left:790px;top:0;width:110px;height:927px"></div>
  <div class="band band--grey" style="left:0;top:182px;width:350px;height:308px"></div>
  <div class="band band--grey" style="left:170px;top:550px;width:68px;height:377px"></div>
  <div class="band band--grey" style="left:410px;top:260px;width:390px;height:100px"></div>
  <div class="band band--grey" style="left:900px;top:230px;width:300px;height:260px"></div>
  <div class="band band--grey" style="left:850px;top:640px;width:350px;height:160px"></div>

  <!-- Row 1 -->
  <header class="section-head" style="left:0;top:42px;width:375px;justify-content:flex-start;padding-left:108px">
    <div class="section-head__bar"></div><div class="section-head__stripe"></div>
    <h2 class="section-head__title">BYOD</h2>
    <svg class="section-head__icon" style="left:278px" viewBox="0 0 50 50" fill="none" stroke="#fff" stroke-width="2.2">
      <rect x="4" y="8" width="42" height="28" rx="2"/><path d="M20 36v6M30 36v6M15 43h20"/><rect x="22" y="12" width="10" height="18" rx="1.5"/><rect x="33" y="16" width="8" height="13" rx="1"/>
    </svg>
  </header>
  <section class="copy" style="left:29px;top:122px;width:340px">
    <p><span class="label">The challenge:</span>&nbsp; Give a person the freedom to bring their favorite device into your network and still ensure a uniform computing environment.</p>
    <p><span class="label">The solution:</span> a virtualized systems professional. Virtual systems (Virtual Machine, Virtual networks, even virtual ports) allow all the flexibility needed to handle any device while providing a uniform landscape to manage.</p>
    <p><span class="label">The result:</span> increased flexibility, management and security of your environment all at the same time.</p>
  </section>

  <header class="section-head" style="left:405px;top:42px;width:370px;justify-content:flex-start;padding-left:20px">
    <div class="section-head__bar"></div><div class="section-head__stripe"></div>
    <h2 class="section-head__title">BACKUP AND<br>DISASTER RECOVERY</h2>
    <svg class="section-head__icon" style="left:288px" viewBox="0 0 50 50" fill="none" stroke="#fff" stroke-width="2.2">
      <rect x="5" y="4" width="40" height="32" rx="2"/><path d="M20 36v6M30 36v6M15 43h20M15 28l14-14M27 12a4 4 0 1 0 5 5M32 28L18 14"/>
    </svg>
  </header>
  <section class="copy" style="left:414px;top:120px;width:370px">
    <p><span class="label">Are you still maintaining a backup and disaster recovery plan?</span>&nbsp; Step up to a Business Continuity plan, a system that lets you keep going no matter what, and all while cutting your costs.</p>
    <p><span class="label">How does it work?</span><br>Instead of just backing up your data, we back up entire servers and then virtualize them so they can run in the Cloud keeping you from having downtime.</p>
    <p class="emphasis" style="margin-bottom:4px">No redundant hardware to buy or maintain, no remote locations to manage, just the smartest solution for expecting the unexpected.</p>
    <p class="callout callout--dark" style="text-align:left;padding-left:56px">Don’t recover from disaster,<br>sail right through it!</p>
  </section>

  <header class="section-head" style="left:803px;top:42px;width:352px;justify-content:flex-start;padding-left:18px">
    <div class="section-head__bar"></div><div class="section-head__stripe"></div>
    <h2 class="section-head__title">CLOUD COMPUTING</h2>
    <svg class="section-head__icon" style="left:262px" viewBox="0 0 50 50" fill="none" stroke="#fff" stroke-width="2.6">
      <path d="M13 38a9 9 0 0 1-1-18 12 12 0 0 1 23-3 10 10 0 0 1 3 21"/><path d="M25 42V24M18 31l7-7 7 7"/>
    </svg>
  </header>
  <section class="copy" style="left:813px;top:120px;width:360px">
    <p>It is becoming increasingly expensive to host your own servers.&nbsp; Cloud solutions not only offer a lower total cost of ownership due to the economy of scale, but are more reliable.</p>
    <p class="callout callout--dark" style="margin-top:-6px;margin-bottom:16px">Imagine email that never goes down and can be accessed from anywhere on any device.</p>
    <p style="margin-bottom:10px"><span class="label">Are you a non-profit or educational institution?</span></p>
    <p>There are programs available that provide these services at little to no cost, let Brightpath Systems help you take advantage today!</p>
  </section>

  <!-- Row 2 -->
  <header class="section-head" style="left:0;top:490px;width:375px;justify-content:flex-start;padding-left:66px">
    <div class="section-head__bar"></div><div class="section-head__stripe"></div>
    <h2 class="section-head__title">TECHNOLOGY<br>&nbsp;&nbsp;TRAINING</h2>
    <svg class="section-head__icon" style="left:266px" viewBox="0 0 50 50" fill="#fff">
      <circle cx="10" cy="10" r="5"/><circle cx="25" cy="8" r="5.5"/><circle cx="40" cy="10" r="5"/>
      <path d="M3 18h14v16h-3v12H6V34H3zM18 16h14v18h-3v14h-8V34h-3zM33 18h14v16h-3v12h-8V34h-3z"/>
    </svg>
  </header>
  <section class="copy" style="left:29px;top:574px;width:340px">
    <p style="margin-bottom:12px">The pace of technology never has people in mind. We all want to make use of the latest technological abilities, but who has the time to learn it all?</p>
    <p class="callout callout--orange" style="margin-bottom:10px">Keeping up is our job and we can help you do it by making sure you only focus on those things you need and don’t waste your time on the things you don’t.</p>
    <p>From dedicated online resources to in person training sessions, we first help you catch up and then take the lead!</p>
  </section>
  <div class="fruit-photo" role="img" aria-label="Photo of a row of red apples with a single orange"></div>

  <header class="section-head" style="left:405px;top:490px;width:370px;justify-content:flex-start;padding-left:32px">
    <div class="section-head__bar"></div><div class="section-head__stripe"></div>
    <h2 class="section-head__title">TOTAL SUPPORT</h2>
    <svg class="section-head__icon" style="left:280px" viewBox="0 0 50 50" fill="none" stroke="#fff" stroke-width="2.4">
      <rect x="14" y="6" width="22" height="16" rx="1.5"/><path d="M25 22v5M19 27h12"/>
      <path d="M3 26l6 12 10 6v4M47 26l-6 12-10 6v4M9 30l6 6M41 30l-6 6"/>
    </svg>
  </header>
  <section class="copy" style="left:414px;top:574px;width:370px">
    <p style="margin-bottom:6px"><span class="label">Don’t go IT alone.</span>&nbsp; We make it simple by offering fast and reliable support for you, as well as Proactive Desktop Remote management and maintenance for you workstations for one monthly fee.</p>
    <p style="margin-bottom:10px">Now you don’t have to worry about racking up bills whenever you need support.</p>
    <p class="callout callout--dark">Our Steady Shield’s proactive managed desktop care provides comprehensive preventative maintenance services, a bundled managed anti-virus package and remote support.</p>
  </section>

  <header class="section-head" style="left:803px;top:490px;width:352px;justify-content:flex-start;padding-left:12px">
    <div class="section-head__bar"></div><div class="section-head__stripe"></div>
    <h2 class="section-head__title">NETWORK SECURITY</h2>
    <svg class="section-head__icon" style="left:270px" viewBox="0 0 50 50" fill="none" stroke="#fff" stroke-width="2">
      <circle cx="34" cy="13" r="9"/><path d="M25 13h18M34 4c-4 5-4 13 0 18M34 4c4 5 4 13 0 18"/>
      <path d="M4 22h40v24H4zM4 30h40M4 38h40M14 22v8M30 22v8M22 30v8M38 30v8M14 38v8M30 38v8"/>
    </svg>
  </header>
  <section class="copy" style="left:813px;top:578px;width:365px">
    <p style="margin-bottom:6px"><span class="label">How Secure is your Network?&nbsp; Are you at risk?</span></p>
    <p class="callout callout--orange" style="text-align:left;padding-left:66px;margin-bottom:8px">It’s time to get proactive.</p>
    <p style="margin-bottom:8px">The Internet offers significant benefits to organizations of all sizes, but with it comes many potent security issues.&nbsp; From Malware to Data Theft, layering protection into your current IT infrastructure is becoming more and more important every day.</p>
    <p class="callout callout--dark">We can help you by reviewing your needs and finding a solution that works best for you.</p>
  </section>
</main>
</body>
</html>
```